Infographic for small business and social media

We are looking for a long term infographics designer to work with, and what a better way to start then with a competition? We want small business relation and social media related inforgraphics done on a fortnightly basis (rates will be re-negotiated for a longer term regular contract). We are looking for someone that can:

Turn content into a visually appealing and easy to understand infographic
Someone with a interesting and funky style (even thought we are about business, we want to have a more innovative image, which is not completely corporate)

Here is the first article to turn into an infographic:

http://www.tradewavehub.com.au/2013/07/25/social-media-offers-revenue-gains-to-small-business-latest-kelp-statistics/

```html
<!DOCTYPE html>
<html lang="en">
<head>
<meta charset="utf-8">
<title>Social media offers revenue gains to small business</title>
<link rel="stylesheet" href="https://fonts.googleapis.com/css2?family=Open+Sans:wght@300;400;700&display=swap">
<style>
:root{
  --green:#3bac4a;
  --sky:#29a6df;
  --blue:#1a6db3;
  --navy:#3b5998;
  --red:#e84b3c;
  --orange:#f7931e;
  --cyan:#3ebfee;
  --white:#ffffff;
  --dark:#1d1d1b;
  --down:#d9241c;
}
*{margin:0;padding:0;box-sizing:border-box}
html,body{width:1200px;height:2700px;overflow:hidden}
body{font-family:"Open Sans",Arial,sans-serif;font-weight:300;color:var(--white);background:var(--green)}
.canvas{position:relative;width:1200px;height:2700px;background:var(--green)}
.abs{position:absolute}
.title{top:24px;left:0;width:1200px;text-align:center;font-size:44px;line-height:57px}
.rule{left:22px;width:1156px;border-top:3px dashed var(--white)}
.intro{top:192px;left:26px;width:1160px;font-size:27.5px;line-height:37px}
.band{position:absolute;left:0;width:1200px}
.band .pct{position:absolute;left:52px;font-size:100px;line-height:1;letter-spacing:-2px}
.band .txt{position:absolute;left:288px;font-size:46px;line-height:57px}
.band .mark{position:absolute;right:18px;bottom:14px;font-weight:700;font-size:40px;line-height:1}
.band-social{top:292px;height:148px;background:var(--green)}
.band-calls{top:442px;height:171px;background:var(--sky)}
.band-network{top:615px;height:170px;background:var(--blue)}
.band-pages{top:787px;height:171px;background:linear-gradient(90deg,var(--navy) 0 600px,var(--red) 600px)}
.band-blog{top:960px;height:169px;background:var(--orange)}
.band-micro{top:1132px;height:171px;background:var(--cyan)}
.band-pages .txt{font-size:34px;line-height:44px;left:284px;top:38px}
.band-blog .mark{font-weight:400;font-size:52px}
.chart-icon{position:absolute;left:50px}
.stat{position:absolute;left:243px;width:920px;font-size:29px;line-height:38px}
.stat b{font-weight:700}
.avatar{top:1775px;left:80px;width:160px;height:150px;background:var(--white);border-radius:80px 80px 14px 14px}
.caption{top:1925px;left:40px;width:240px;text-align:center;font-size:30px;line-height:38px;font-weight:400}
.quote{top:1784px;left:343px;width:705px;font-size:29px;line-height:37.5px;text-align:justify}
.qmark{font-family:"Open Sans",Arial,sans-serif;font-weight:700;font-size:110px;line-height:1}
.body-text{font-size:29px;line-height:38px}
.body-text b{font-weight:700}
.bar-label{font-size:12px;font-weight:700;line-height:1}
.big{font-size:86px;line-height:1;letter-spacing:-2px}
.pay{font-size:30px;line-height:38px}
.pay b{font-weight:700}
</style>
</head>
<body>
<div class="canvas">
  <h1 class="abs title">Social media offers revenue gains to small business:<br>latest Kelp statistics</h1>
  <div class="abs rule" style="top:167px"></div>
  <p class="abs intro">Social media use is on the rise amongst Australian small and medium businesses (SMEs) and can benefit their revenue levels, according to the latest research from Kelp.</p>

  <section class="band band-social">
    <div class="pct" style="top:22px">20%</div>
    <p class="txt" style="top:12px">20% of SMEs surveyed were using social<br>media for business purposes.</p>
  </section>
  <section class="band band-calls">
    <div class="pct" style="top:34px">19%</div>
    <p class="txt" style="top:24px">were using services such as Callio or VOIP<br>to make free business phone calls.</p>
    <span class="mark">Callio</span>
  </section>
  <section class="band band-network">
    <div class="pct" style="top:34px">18%</div>
    <p class="txt" style="top:24px">were doing their business networking<br>online via Linkboard.</p>
    <span class="mark" style="color:var(--dark)">Linkboard</span>
  </section>
  <section class="band band-pages">
    <div class="pct" style="top:34px">16%</div>
    <p class="txt">are connecting with customers or fans via<br>a business page on Friendlio, Vidstream or Circleplus.</p>
    <span class="mark" style="top:14px;bottom:auto;font-size:34px">Vidstream · Circleplus</span>
    <span class="mark" style="left:560px;right:auto;bottom:8px;font-size:24px">Friendlio</span>
  </section>
  <section class="band band-blog">
    <div class="pct" style="top:34px">9%</div>
    <p class="txt" style="top:24px">are sharing news and updates via a<br>company blog.</p>
    <span class="mark">blog</span>
  </section>
  <section class="band band-micro">
    <div class="pct" style="top:34px">6%</div>
    <p class="txt" style="top:24px">communicating via micro-blogging<br>sites such as Chirper.</p>
    <span class="mark">Chirper</span>
  </section>

  <svg class="chart-icon" style="top:1342px" width="165" height="106" viewBox="0 0 165 106" aria-hidden="true">
    <g stroke="#fff" stroke-width="2" fill="none">
      <rect x="1" y="1" width="163" height="104"/>
      <path d="M21 1V105M41 1V105M61 1V105M82 1V105M102 1V105M123 1V105M143 1V105M1 21H164M1 42H164M1 63H164M1 84H164"/>
    </g>
    <polyline points="4,94 40,58 62,74 100,36 118,50 162,4" fill="none" stroke="#fff" stroke-width="4"/>
  </svg>
  <p class="stat" style="top:1358px">The good news for those social-savvy SMEs was that they were more likely to see a rise in their revenue in the year to February 2013.</p>

  <svg class="chart-icon" style="top:1477px" width="165" height="106" viewBox="0 0 165 106" aria-hidden="true">
    <g stroke="#fff" stroke-width="2" fill="none">
      <rect x="1" y="1" width="163" height="104"/>
      <path d="M21 1V105M41 1V105M61 1V105M82 1V105M102 1V105M123 1V105M143 1V105M1 21H164M1 42H164M1 63H164M1 84H164"/>
    </g>
    <polyline points="4,94 40,58 62,74 100,36 118,50 162,4" fill="none" stroke="var(--dark)" stroke-width="4"/>
  </svg>
  <p class="stat" style="top:1492px"><b>28%</b> of SMEs using social media reported an increase in revenue, compared to an average of <b>18%</b> across all SMEs.</p>

  <svg class="chart-icon" style="top:1608px" width="165" height="106" viewBox="0 0 165 106" aria-hidden="true">
    <g stroke="#fff" stroke-width="2" fill="none">
      <rect x="1" y="1" width="163" height="104"/>
      <path d="M21 1V105M41 1V105M61 1V105M82 1V105M102 1V105M123 1V105M143 1V105M1 21H164M1 42H164M1 63H164M1 84H164"/>
    </g>
    <polyline points="2,2 40,46 62,30 100,68 118,52 162,100" fill="none" stroke="var(--down)" stroke-width="4"/>
  </svg>
  <p class="stat" style="top:1623px"><b>18%</b> of SMEs using social media were less likely to report a fall in revenue, compared to an average of <b>39%</b> across all SMEs.</p>

  <div class="abs rule" style="top:1746px"></div>

  <div class="abs avatar" role="img" aria-label="Silhouette portrait of the Kelp CEO"></div>
  <p class="abs caption">Kelp CEO<br>Sam Calder</p>
  <span class="abs qmark" style="top:1764px;left:262px">“</span>
  <blockquote class="abs quote">One in five business owners now wear an additional hat – social media manager. Those who embrace that role are reaping rewards beyond building closer relationships with customers, suppliers, partners and others. The financial benefits are clear.</blockquote>
  <span class="abs qmark" style="top:1906px;left:1056px">”</span>

  <div class="abs rule" style="top:2024px"></div>
  <p class="abs body-text" style="top:2066px;left:26px;width:1160px">Moving beyond social media, the Kelp research also supports recent NSB findings that online engagement is generally low amongst SMEs, with just <b>38%</b> having a website.</p>

  <svg class="abs" style="top:2196px;left:40px" width="390" height="112" viewBox="0 0 390 112" aria-hidden="true">
    <path d="M20 58V12H165M100 48H165" stroke="#fff" stroke-width="2" fill="none"/>
    <rect x="2" y="58" width="33" height="50" fill="#fff"/>
    <rect x="42" y="36" width="34" height="72" fill="#fff"/>
    <text x="4" y="89" font-family="Open Sans,Arial,sans-serif" font-size="13" font-weight="700" fill="var(--green)">37%</text>
    <text x="44" y="72" font-family="Open Sans,Arial,sans-serif" font-size="13" font-weight="700" fill="var(--green)">45%</text>
  </svg>
  <span class="abs bar-label" style="top:2202px;left:206px">conversion rate for sales leads</span>
  <span class="abs bar-label" style="top:2238px;left:206px">customer leads</span>
  <p class="abs body-text" style="top:2192px;left:432px;width:760px">The SMEs that do have a website reported a number of flow on benefits, including increased customer leads and a better conversion rate for sales leads.</p>
  <p class="abs body-text" style="top:2360px;left:34px"><b>1/5</b> said that their website made them more competitive in their market.</p>

  <div class="abs rule" style="top:2436px"></div>
  <div class="abs big" style="top:2462px;left:50px">12%</div>
  <p class="abs body-text" style="top:2472px;left:230px;width:960px">of SMEs sell products and services online directly to customers using their own website. When it comes to accepting online payments :</p>

  <svg class="abs" style="top:2586px;left:228px" width="42" height="68" viewBox="0 0 42 68" aria-hidden="true">
    <rect x="3" y="3" width="36" height="62" rx="6" fill="none" stroke="#fff" stroke-width="5"/>
    <rect x="9" y="12" width="24" height="38" fill="#fff"/>
    <circle cx="21" cy="57" r="3" fill="#fff"/>
  </svg>
  <p class="abs pay" style="top:2578px;left:288px"><b>9%</b> allow payments<br>through a mobile app.</p>
  <div class="abs" style="top:2574px;left:600px;height:96px;border-left:3px solid #fff"></div>
  <svg class="abs" style="top:2584px;left:618px" width="96" height="76" viewBox="0 0 96 76" aria-hidden="true">
    <path d="M2 6H16L26 50H82L92 14H20" fill="none" stroke="#fff" stroke-width="5" stroke-linejoin="round"/>
    <path d="M34 14V50M48 14V50M62 14V50M76 14V50M22 26H89M24 38H86" stroke="#fff" stroke-width="3"/>
    <circle cx="34" cy="66" r="7" fill="#fff"/>
    <circle cx="74" cy="66" r="7" fill="#fff"/>
  </svg>
  <p class="abs pay" style="top:2578px;left:732px"><b>11%</b> of SMEs do this with<br>a shopping cart.</p>
</div>
</body>
</html>
```